Steadfast Care - Need Stationary Design

We need a stationary pack for our new Care company based in the uk
Are corporate colours are Pink and purple
Please use attached logo
Target Market(s)
The Care Industry
Industry/Entity Type
It Company
Contact Information for Business Card
Melissa Rowden
Director

```html
<!DOCTYPE html>
<html lang="en">
<head>
<meta charset="utf-8">
<title>Steadfast Care — Business Card</title>
<link href="https://fonts.googleapis.com/css2?family=Montserrat:wght@400;700&display=swap" rel="stylesheet">
<style>
  :root {
    --purple: #9350b8;
    --purple-deep: #7e3fa3;
    --pink: #e9269b;
    --cream: #f1eee3;
    --ink: #3a3a3a;
    --white: #f7f4ec;
    --backdrop: #d9d6d2;
  }
  html, body {
    margin: 0;
    width: 1200px;
    height: 786px;
    overflow: hidden;
    background: var(--backdrop);
    font-family: "Montserrat", sans-serif;
  }
  .stage {
    width: 1200px;
    height: 786px;
    display: flex;
    align-items: center;
    justify-content: center;
    gap: 50px;
  }
  .card {
    position: relative;
    width: 525px;
    height: 300px;
    border-radius: 18px;
    overflow: hidden;
    box-shadow: 0 6px 18px rgba(0,0,0,.18);
  }
  .card-front { background: var(--cream); }
  .card-back { background: var(--purple); }
  .front-wave { position: absolute; inset: 0; }
  .brand-name {
    margin: 0;
    font-weight: 700;
    letter-spacing: .5px;
    display: flex;
    align-items: center;
    gap: 10px;
  }
  .brand-mark {
    width: 14px;
    height: 14px;
    border-radius: 50%;
    display: inline-block;
  }
  .card-front .brand-name {
    position: absolute;
    left: 40px;
    top: 70px;
    font-size: 26px;
    color: var(--purple);
  }
  .card-front .brand-mark { background: var(--pink); }
  .contact {
    position: absolute;
    left: 275px;
    top: 130px;
    color: var(--ink);
    font-size: 12px;
    line-height: 1.5;
  }
  .contact-name {
    margin: 0;
    font-weight: 700;
    font-size: 15px;
    color: var(--purple);
    letter-spacing: .5px;
  }
  .contact-role { margin: 0 0 8px; font-size: 12px; }
  .contact-line { display: flex; align-items: center; gap: 7px; margin: 0; }
  .contact-icon {
    width: 13px; height: 13px; border-radius: 3px;
    background: var(--pink); flex: none;
  }
  .contact-address { margin: 6px 0 0; }
  .card-back {
    display: flex;
    align-items: center;
    justify-content: center;
  }
  .card-back .brand-name { font-size: 32px; color: var(--white); }
  .card-back .brand-mark { background: var(--white); width: 18px; height: 18px; }
</style>
</head>
<body>
<main class="stage">
  <section class="card card-front">
    <svg class="front-wave" viewBox="0 0 525 300" aria-hidden="true">
      <path d="M0 175 C 90 215, 190 230, 250 300 L 0 300 Z" fill="var(--purple)" opacity=".25"/>
      <path d="M0 190 C 110 225, 200 245, 240 300 L 0 300 Z" fill="var(--purple)"/>
      <path d="M0 165 C 110 200, 215 225, 270 300" fill="none" stroke="var(--pink)" stroke-width="6"/>
    </svg>
    <h1 class="brand-name"><span class="brand-mark"></span>Steadfast Care</h1>
    <div class="contact">
      <p class="contact-name">OWEN MARSH</p>
      <p class="contact-role">General Manager</p>
      <p class="contact-line"><svg class="contact-icon" viewBox="0 0 13 13"><rect width="13" height="13" rx="3" fill="var(--pink)"/><path d="M4 3 l2 2 -1 1 q1 2 2 2 l1-1 2 2 -1 1 q-4 0 -6 -6z" fill="#fff"/></svg>+44 1632 960 418</p>
      <p class="contact-line"><svg class="contact-icon" viewBox="0 0 13 13"><rect width="13" height="13" rx="3" fill="var(--pink)"/><rect x="3" y="4" width="7" height="5" fill="none" stroke="#fff"/><path d="M3 4 l3.5 3 3.5-3" fill="none" stroke="#fff"/></svg>info@steadfastcare.co.uk</p>
      <p class="contact-line"><svg class="contact-icon" viewBox="0 0 13 13"><rect width="13" height="13" rx="3" fill="var(--pink)"/><circle cx="6.5" cy="6.5" r="3.5" fill="none" stroke="#fff"/><path d="M3 6.5 h7" stroke="#fff"/></svg>www.steadfastcare.co.uk</p>
      <p class="contact-address">B12 Elm Court, Elm Park<br>Hartwell, HW3 7QS</p>
    </div>
  </section>
  <section class="card card-back">
    <h2 class="brand-name"><span class="brand-mark"></span>Steadfast Care</h2>
  </section>
</main>
</body>
</html>
```